Website for Velmorund Capital, my new firm that raises money from investors to buy, build, own an...

Velmorund Capital needs a website! We are a new company with very experienced people, who invest in, own and build hotel properties, as well as apartments and other commercial real estate. We seek investors for our projects, and we provide safe, secure returns on their investment in our projects. Our new logo is designed to exhibit strength, class and security, and would like our website to continue on this theme. Our name, Velmorund, is a word-play on a Greek word “aristeia”, which means “excellence” and “a warriors finest moment of glory in war”. If you are in business, you realize that much of it is like war, with strategy and moves and opponents and competitors, and ever-changing economic conditions and threats that make business very much like war. We like to think that we are good at business (war), and so have named our company “Velmorund”, using the founders last name and the word “aristeia” combined. Another definition of "aristeia" is "performing at the peak of one's potential after a long struggle"...again, much like business in real life! The website design should exhibit financial security, smart moves, and positive growth towards a bright future.

Target Market(s)

The target market is smart and wealthy investors, with others such as brokers, cities and government agencies, lenders, sellers, partners, etc also looking at it.

Industry/Entity Type

Investment

Number of Pages Required

5+ page

Font styles to use
Sans Serif

Colors
fec214

Requirements
Must have
• Our website should have a landing page, a "about" or bio page, a projects page and a contact us page. Our new logo uses the colors black and gold, so this should be factored in to our site. The site should be simple, yet impactful and impressive. I have actually two logos, which can be mixed and interchanged in a complimentary way, each with their own unique look.
Nice to have
• I have uploaded a couple screenshots of a website i like, and the simplicity I mention.
Should not have
• The site should not be flashy or complicated or complex or "busy"

```html
<!DOCTYPE html>
<html lang="en">
<head>
<meta charset="utf-8">
<title>Velmorund Capital</title>
<link href="https://fonts.googleapis.com/css2?family=Montserrat:wght@300;400;500;600;700&display=swap" rel="stylesheet">
<style>
:root{
  --gold:#fec214;
  --gold-deep:#c9962a;
  --ink:#2a2a2a;
  --muted:#777a80;
  --soft:#f4f5f9;
  --white:#ffffff;
  --price:#d6453c;
  --line:#e4e5ea;
}
*{box-sizing:border-box;margin:0;padding:0}
html,body{width:1200px;height:2683px;overflow:hidden}
body{font-family:'Montserrat',sans-serif;color:var(--ink);background:var(--soft);position:relative}
section,header,footer{position:absolute;left:0;width:1200px}
.abs{position:absolute}

/* hero */
.hero{top:0;height:565px;background:linear-gradient(180deg,#5a6fa6 0%,#9a86b4 30%,#c98fa8 45%,#4f6a9c 70%,#24324e 100%)}
.hero-photo{position:absolute;inset:0}
.brand{position:absolute;left:66px;top:44px;display:flex;align-items:center;gap:10px;color:var(--white);font-weight:600;font-size:20px;letter-spacing:2px}
.brand-mark{width:14px;height:14px;border:2px solid var(--white)}
.nav{position:absolute;left:440px;top:56px;display:flex;gap:26px;font-size:10px;font-weight:600;letter-spacing:1px;color:var(--white)}
.nav .active{color:var(--gold)}
.nav-call{position:absolute;left:964px;top:56px;font-size:10px;font-weight:600;letter-spacing:1px;color:var(--gold)}
.hero-title{position:absolute;top:270px;width:100%;text-align:center;color:var(--white);font-size:33px;font-weight:600;line-height:42px;text-shadow:0 2px 8px rgba(0,0,0,.25)}
.hero-label{position:absolute;top:497px;width:100%;text-align:center;color:var(--white);font-size:9px;letter-spacing:1.5px}

/* featured */
.featured{top:565px;height:630px;background:var(--soft)}
.arrow{position:absolute;top:262px;color:#9ca0a8;font-size:16px}
.card{position:absolute;top:55px;width:282px;height:431px;background:var(--white);box-shadow:0 3px 14px rgba(0,0,0,.08)}
.card-photo{height:161px}
.card-body{padding:0 21px}
.card h3{margin-top:32px;font-size:16px;font-weight:400}
.card .loc{margin-top:4px;font-size:8px;letter-spacing:.8px;color:var(--muted)}
.card .desc{margin-top:18px;font-size:9.5px;line-height:16px;color:var(--muted);height:48px}
.card .rule{margin-top:16px;border-top:1px solid var(--line)}
.card .from{margin-top:14px;font-size:9.5px;color:var(--muted)}
.card .price{font-size:15px;font-weight:600;color:var(--price);margin-top:2px}
.card .ring{position:absolute;right:24px;top:306px;width:44px;height:44px}
.card .ring span{position:absolute;inset:0;display:flex;align-items:center;justify-content:center;font-size:9px;color:var(--muted)}
.card .sold{position:absolute;right:16px;top:282px;background:var(--gold-deep);color:var(--white);font-size:8px;font-weight:600;letter-spacing:.8px;padding:4px 12px;border-radius:10px}
.card .enquire{position:absolute;left:21px;top:378px;width:120px;height:36px;background:var(--gold);font-size:9px;font-weight:700;letter-spacing:.8px;display:flex;align-items:center;justify-content:center}
.card .net{position:absolute;right:21px;top:380px;text-align:right;font-size:13px}
.card .net small{display:block;font-size:8px;color:var(--muted);margin-top:3px}
.discover{position:absolute;top:540px;width:100%;text-align:center;font-size:11px}
.discover a{display:block;margin-top:8px;color:var(--gold-deep);font-size:12px;text-decoration:underline}

/* philosophy */
.philosophy{top:1195px;height:388px;background:var(--white)}
.philosophy-photo{position:absolute;left:0;top:0;width:599px;height:388px;background:linear-gradient(135deg,#3e5068 0%,#20262e 45%,#9aa3ad 75%,#d8cfc4 100%)}
.eyebrow{font-size:9px;font-weight:600;letter-spacing:1.5px;color:var(--gold-deep)}
.eyebrow-rule{width:28px;border-top:1px solid var(--gold-deep);margin-top:10px}
.phil-text{position:absolute;left:670px;top:57px;width:450px}
.phil-text h2{margin-top:20px;font-size:24px;font-weight:400;line-height:32px}
.phil-text p{margin-top:18px;font-size:10px;line-height:17px;color:var(--muted)}
.btn{background:var(--gold);font-size:9px;font-weight:700;letter-spacing:.8px;display:flex;align-items:center;justify-content:center;width:120px;height:34px}
.phil-text .btn{margin-top:42px}

/* services */
.services{top:1583px;height:420px;background:var(--soft);text-align:center}
.services .eyebrow{position:absolute;top:56px;width:100%}
.services .eyebrow-rule{position:absolute;top:74px;left:586px;margin:0}
.services h2{position:absolute;top:98px;width:100%;font-size:25px;font-weight:400}
.service{position:absolute;top:175px;width:220px;margin-left:-110px}
.service svg{width:26px;height:26px}
.service h4{margin-top:10px;font-size:12px;font-weight:500}
.service p{margin-top:8px;font-size:9.5px;line-height:15px;color:var(--muted)}
.services .btn{position:absolute;left:540px;top:327px}

/* register */
.register{top:2003px;height:388px;background:linear-gradient(160deg,#6c7f96 0%,#2b3a4f 40%,#1a2435 70%,#5d6e84 100%)}
.register h2{position:absolute;top:60px;width:100%;text-align:center;color:var(--white);font-size:25px;font-weight:400}
.register .sub{position:absolute;top:90px;width:100%;text-align:center;color:var(--white);font-size:10px}
.field{position:absolute;left:311px;width:281px;height:35px;background:var(--white);font-size:9px;color:#9a9da3;padding:12px 14px}
.message{position:absolute;left:608px;top:128px;width:281px;height:131px;background:var(--white);font-size:9px;color:#9a9da3;padding:12px 14px}
.register .btn{position:absolute;left:540px;top:291px}

/* footer */
.site-footer{top:2391px;height:292px;background:var(--soft);text-align:center}
.footer-brand{position:absolute;top:60px;width:100%;font-size:22px;font-weight:500;letter-spacing:2px}
.footer-call{position:absolute;top:120px;width:100%;font-size:12px;color:var(--muted)}
.footer-call b{color:var(--ink);font-weight:600}
.socials{position:absolute;top:150px;left:0;width:100%;display:flex;justify-content:center;gap:9px}
.socials span{width:30px;height:30px;border-radius:50%;background:#e8e9ee}
.socials .on{background:var(--gold)}
.copy{position:absolute;top:209px;width:100%;font-size:8px;letter-spacing:.6px;color:var(--muted)}
.legal{position:absolute;top:226px;width:100%;font-size:8px;color:var(--muted)}
</style>
</head>
<body>

<header class="hero">
  <div class="hero-photo" role="img" aria-label="Waterfront luxury apartment tower with rooftop pool at dusk"></div>
  <div class="brand"><span class="brand-mark"></span>VELMORUND</div>
  <nav class="nav">
    <span class="active">PHILOSOPHY</span><span>DEALS</span><span>SERVICES</span><span>TEAM</span><span>INTELLIGENCE</span><span>CONTACT</span>
  </nav>
  <div class="nav-call">CALL: &#9743; +44 (0) 207 555 0184</div>
  <h1 class="hero-title">Delivering An Intelligent Property<br>Investment Service</h1>
  <div class="hero-label">FEATURED PROPERTIES</div>
</header>

<section class="featured">
  <span class="arrow" style="left:126px">&#8249;</span>
  <span class="arrow" style="left:1064px">&#8250;</span>

  <article class="card" style="left:163px">
    <div class="card-photo" role="img" aria-label="Modern bedroom interior with city view" style="background:linear-gradient(135deg,#3a3d44,#8a8e96 60%,#d5d2cc)"></div>
    <div class="card-body">
      <h3>Weaver Quarter Residence</h3>
      <div class="loc">&#9679; LIVERPOOL, UNITED KINGDOM</div>
      <p class="desc">FREE Furniture Pack. Luxury City Centre Buy-to-Let Apartments. Hassle-Free. 8% Rental Assurance.</p>
      <div class="rule"></div>
      <div class="from">Available from:</div>
      <div class="price">$94,200</div>
    </div>
    <svg class="ring" viewBox="0 0 44 44"><circle cx="22" cy="22" r="20" fill="none" stroke="#eceef2" stroke-width="2"/><circle cx="22" cy="22" r="20" fill="none" stroke="#c9962a" stroke-width="2" stroke-dasharray="94.2 125.7" transform="rotate(-90 22 22)"/></svg>
    <div class="ring"><span>75%</span></div>
    <div class="enquire">ENQUIRE NOW!</div>
    <div class="net">8% NET<small>Assured for 3 years</small></div>
  </article>

  <article class="card" style="left:459px">
    <div class="card-photo" role="img" aria-label="Brick apartment building at night" style="background:linear-gradient(180deg,#2e3a8c,#4a56a8 55%,#3b3142)"></div>
    <div class="card-body">
      <h3>Harbour Lane Court</h3>
      <div class="loc">&#9679; PLYMOUTH, USA</div>
      <p class="desc">NEW Luxury Student Apartments. Hassle-Free. 6% NET Rental Assurance. City Centre Location.</p>
      <div class="rule"></div>
      <div class="from">Available from:</div>
      <div class="price">$71,300</div>
    </div>
    <div class="sold">SOLD OUT</div>
    <svg class="ring" viewBox="0 0 44 44"><circle cx="22" cy="22" r="20" fill="none" stroke="#eceef2" stroke-width="2"/><circle cx="22" cy="22" r="20" fill="none" stroke="#c9962a" stroke-width="2" stroke-dasharray="62.8 125.7" transform="rotate(-90 22 22)"/></svg>
    <div class="ring"><span>50%</span></div>
    <div class="enquire">ENQUIRE NOW!</div>
    <div class="net">6% NET<small>Assured for 2 years</small></div>
  </article>

  <article class="card" style="left:756px">
    <div class="card-photo" role="img" aria-label="Bright living room with sofa and large windows" style="background:linear-gradient(135deg,#6b5a48,#b9ab98 55%,#e2dcd2)"></div>
    <div class="card-body">
      <h3>Meadowbank Care Village</h3>
      <div class="loc">&#9679; LANCASHIRE, NZ</div>
      <p class="desc">NEW Luxury Student Apartments. Hassle-Free. 8% NET Rental Assurance. City Centre Location.</p>
      <div class="rule"></div>
      <div class="from">Available from:</div>
      <div class="price">$82,600</div>
    </div>
    <svg class="ring" viewBox="0 0 44 44"><circle cx="22" cy="22" r="20" fill="none" stroke="#c9962a" stroke-width="2"/></svg>
    <div class="ring"><span>100%</span></div>
    <div class="enquire">ENQUIRE NOW!</div>
    <div class="net">8% NET<small>Assured for 5 years</small></div>
  </article>

  <div class="discover">Discover your next great investment for your property portfolio.<a>View our full property portfolio</a></div>
</section>

<section class="philosophy">
  <div class="philosophy-photo" role="img" aria-label="Hands holding a tablet showing a luxury bathroom interior"></div>
  <div class="phil-text">
    <div class="eyebrow">OUR PHILOSOPHY</div>
    <div class="eyebrow-rule"></div>
    <h2>We are proud to be the home<br>of property experts.</h2>
    <p>Lorem ipsum dolor sit amet, consectetur adipiscing elit, sed do eiusmod tempor incididunt ut labore et dolore magna aliqua. Ut enim ad minim veniam, quis nostrud exercitation ullamco laboris nisi ut aliquip ex ea commodo consequat. Duis aute irure dolor in reprehenderit in voluptate velit esse cillum dolore eu fugiat nulla pariatur. Excepteur sint occaecat cupidatat non proident.</p>
    <div class="btn">ABOUT US</div>
  </div>
</section>

<section class="services">
  <div class="eyebrow">CUSTOMER SERVICE</div>
  <div class="eyebrow-rule"></div>
  <h2>Take the load off your shoulders</h2>

  <div class="service" style="left:261px">
    <svg viewBox="0 0 24 24" fill="none" stroke="#a8abb2" stroke-width="2"><circle cx="10" cy="10" r="6"/><path d="M15 15l6 6"/></svg>
    <h4>Property Sourcing</h4>
    <p>Lorem Ipsum is simply dummy text adipiscing elit, sed do eiusmod tempor incididunt ut.</p>
  </div>
  <div class="service" style="left:486px">
    <svg viewBox="0 0 24 24" fill="#a8abb2"><path d="M12 3l10 9h-3v9h-5v-6h-4v6H5v-9H2z"/></svg>
    <h4>Property Sales</h4>
    <p>Lorem Ipsum is simply dummy text adipiscing elit, sed do eiusmod tempor incididunt ut.</p>
  </div>
  <div class="service" style="left:712px">
    <svg viewBox="0 0 24 24" fill="none" stroke="#a8abb2" stroke-width="1.8"><rect x="3" y="3" width="18" height="18"/><path d="M8 7h2M14 7h2M8 11h2M14 11h2M8 15h2M14 15h2"/></svg>
    <h4>Letting &amp; Management</h4>
    <p>Lorem Ipsum is simply dummy text adipiscing elit, sed do eiusmod tempor incididunt ut.</p>
  </div>
  <div class="service" style="left:937px">
    <svg viewBox="0 0 24 24" fill="#a8abb2"><path d="M12 2l10 5-10 5L2 7z"/><path d="M2 12l10 5 10-5v3l-10 5-10-5z" opacity=".7"/></svg>
    <h4>Portfolio Management</h4>
    <p>Lorem Ipsum is simply dummy text adipiscing elit, sed do eiusmod tempor incididunt ut.</p>
  </div>

  <div class="btn">CONTACT US</div>
</section>

<section class="register">
  <div class="abs" style="inset:0" role="img" aria-label="Upward view of city skyscrapers and a broadcast tower"></div>
  <h2>Register Your Interest</h2>
  <div class="sub">Our Investment Experts are ready to help you in your investment search.</div>
  <div class="field" style="top:128px">your name</div>
  <div class="field" style="top:176px">Email</div>
  <div class="field" style="top:223px">Phone</div>
  <div class="message">Type your message ...</div>
  <div class="btn">SUBMIT</div>
</section>

<footer class="site-footer">
  <div class="footer-brand">VELMORUND CAPITAL</div>
  <div class="footer-call"><b>Call:</b> &#9743; +44 (0) 207 555 0184, <b>E.</b> info@velmorundcapital.com</div>
  <div class="socials"><span></span><span class="on"></span><span></span><span></span></div>
  <div class="copy">© VELMORUND CAPITAL. ALL RIGHTS RESERVED.</div>
  <div class="legal">Terms &amp; Conditions &nbsp;|&nbsp; Privacy Policy</div>
</footer>

</body>
</html>
```